Klerovan Disinfecting company

Company name: Klerovan Inc
We are starting up a new company that is a professional spray disinfecting company. We will be offering a service where we go into facilities like residential, office, child care, medical, dental, restaurant, entertainment, hotel/motel, automotive fleets with professional spraying equipment and disinfect their facilities for a fee. Our products kills a wide range of viruses and pathogens including Covid 19.

Target Market(s)

Residential, commercial office space, child care, medical, dental, restaurant, entertainment facilities, hotel/motel, automotive fleets.

Font styles to use
Sans Serif

Colors
31b7a3

Requirements
Must have
• Company name - Klerovan Inc
Phone - 555-847-2936
Email - tormelvax@brintova.com
Our Slogan - Disinfect Today For A Safe Tomorrow
Brief description of our reservice
Nice to have
• Some kind of a picture of a man with a sprayer, perhaps in a white coveralls, perhaps on a background of a few of the facilities in mention in my target market section. I have uploaded 4 examples of print ads form similar companies. I don't necessarily want them to look alike however these are very professional ads and will give you the gist of what I'm looking for.

```html
<!DOCTYPE html>
<html lang="en">
<head>
<meta charset="utf-8">
<title>Klerovan Inc – Disinfect Today For A Safe Tomorrow</title>
<link href="https://fonts.googleapis.com/css2?family=Montserrat:wght@300;400;500;600;700;800;900&display=swap" rel="stylesheet">
<style>
:root{
  --blue:#0a74c8;
  --teal:#31b7a3;
  --teal-soft:#8fd9cc;
  --ink:#1f2328;
  --white:#ffffff;
  --paper:#f3f4f5;
}
*{margin:0;padding:0;box-sizing:border-box}
html,body{width:933px;height:1200px;overflow:hidden;background:var(--white)}
body{font-family:"Montserrat",Arial,sans-serif;color:var(--ink)}
.flyer{position:relative;width:933px;height:1200px;overflow:hidden}
.backdrop{position:absolute;inset:0;width:933px;height:1200px}
.abs{position:absolute;white-space:nowrap}

.brand{left:57px;top:66px;font-size:52px;font-weight:800;color:var(--white);letter-spacing:-0.5px;line-height:60px}

.slogan-word{left:55px;font-weight:800;color:var(--white);line-height:1}
.slogan-disinfect{top:181px;font-size:68px;letter-spacing:-0.5px}
.slogan-box{position:absolute;left:57px;background:var(--teal);border-radius:3px}
.slogan-today{top:258px;width:275px;height:55px}
.slogan-today span{position:absolute;left:44px;top:3px;font-size:49px;line-height:1;font-weight:800;color:var(--white)}
.slogan-fora{top:322px;font-size:50px;font-weight:400}
.slogan-safe{left:226px;top:316px;font-size:74px;letter-spacing:-1px}
.slogan-tomorrow{top:400px;width:375px;height:67px}
.slogan-tomorrow span{position:absolute;left:19px;top:7px;font-size:50px;line-height:1;font-weight:800;color:var(--white)}

.pitch{left:56px;top:608px;font-size:34px;line-height:47px;font-weight:300;color:var(--ink)}
.pitch b{font-weight:700;color:var(--blue)}
.pitch .teal{font-weight:700;color:#2a9f86}

.service{position:absolute;width:134px;text-align:center}
.service svg{display:block;margin:0 auto;width:50px;height:50px}
.service .rule{height:2px;background:var(--blue);margin-top:6px}
.service .label{font-size:16.5px;font-weight:500;margin-top:9px;white-space:nowrap}

.call{left:28px;top:1066px;font-size:44px;font-weight:800;color:var(--white);letter-spacing:1px}
.phone{left:30px;top:1136px;font-size:47px;font-weight:800;color:var(--blue);display:flex;align-items:center;gap:8px}
.phone svg{width:42px;height:42px}
.tagline{right:43px;top:1064px;font-size:18.5px;line-height:24px;font-weight:700;color:var(--blue);text-align:right}
.email{left:521px;top:1143px;font-size:26px;font-weight:500;color:var(--white);display:flex;align-items:center;gap:10px}
.email svg{width:32px;height:32px}
</style>
</head>
<body>
<main class="flyer">
  <svg class="backdrop" viewBox="153 191 1095 1416" preserveAspectRatio="none">
    <defs>
      <linearGradient id="paperFade" x1="0" y1="0" x2="1" y2="1">
        <stop offset="0" stop-color="#eceeef"/>
        <stop offset="0.6" stop-color="#f7f8f8"/>
        <stop offset="1" stop-color="#ffffff"/>
      </linearGradient>
      <linearGradient id="officeTone" x1="0" y1="0" x2="1" y2="1">
        <stop offset="0" stop-color="#e9e3d8"/>
        <stop offset="0.5" stop-color="#f2f0ec"/>
        <stop offset="1" stop-color="#c9c4bb"/>
      </linearGradient>
      <linearGradient id="gymTone" x1="0" y1="0" x2="1" y2="1">
        <stop offset="0" stop-color="#3c4044"/>
        <stop offset="0.45" stop-color="#9aa0a5"/>
        <stop offset="1" stop-color="#2b2e31"/>
      </linearGradient>
      <clipPath id="sheet"><rect x="153" y="191" width="1095" height="1416"/></clipPath>
    </defs>
    <g clip-path="url(#sheet)">
      <rect x="153" y="191" width="1095" height="1416" fill="url(#paperFade)"/>
      <circle class="hero-field" cx="450" cy="417" r="445" fill="var(--blue)"/>
      <circle cx="450" cy="430" r="445" fill="none" stroke="var(--teal)" stroke-width="1.5" opacity="0.6"/>
      <circle cx="1055" cy="453" r="382" fill="var(--white)"/>
      <circle cx="1055" cy="453" r="382" fill="none" stroke="var(--teal)" stroke-width="1.5"/>
      <circle cx="1055" cy="453" r="367" fill="url(#officeTone)" role="img" aria-label="Photo: technician in white coveralls spraying disinfectant in an office"/>
      <circle cx="780" cy="822" r="60" fill="var(--teal-soft)" opacity="0.85"/>
      <circle cx="972" cy="940" r="226" fill="none" stroke="var(--teal)" stroke-width="1.5"/>
      <circle cx="972" cy="940" r="216" fill="url(#gymTone)" role="img" aria-label="Photo: technician with backpack sprayer disinfecting gym treadmills"/>
      <polygon class="call-band" points="153,1445 713,1445 760,1522 153,1522" fill="var(--teal)"/>
      <polygon class="contact-band" points="752,1522 1248,1522 1248,1607 810,1607" fill="var(--blue)"/>
    </g>
  </svg>

  <div class="abs brand">Klerovan Inc</div>

  <div class="abs slogan-word slogan-disinfect">DISINFECT</div>
  <div class="slogan-box slogan-today"><span>TODAY</span></div>
  <div class="abs slogan-word slogan-fora">FOR A</div>
  <div class="abs slogan-word slogan-safe">SAFE</div>
  <div class="slogan-box slogan-tomorrow"><span>TOMORROW</span></div>

  <p class="abs pitch">Our products <b>Kills</b><br>a wide range of <b>Viruses</b><br><span class="teal">and pathogens</span><br><b>Including Covid 19.</b></p>

  <div class="service" style="left:64px;top:830px">
    <svg viewBox="0 0 50 50" fill="none" stroke="var(--teal)" stroke-width="1.8"><path d="M4 24 25 6l21 18M9 20v26h32V20"/><rect x="20" y="32" width="10" height="14"/><path d="M36 9v7"/></svg>
    <div class="rule"></div><div class="label">Residential</div>
  </div>
  <div class="service" style="left:250px;top:830px">
    <svg viewBox="0 0 50 50" fill="none" stroke="var(--teal)" stroke-width="1.8"><rect x="6" y="4" width="38" height="10"/><path d="M12 4v10M18 4v10M24 4v10M30 4v10M36 4v10M8 14v32h34V14"/><rect x="12" y="22" width="18" height="16"/><rect x="33" y="24" width="6" height="22"/></svg>
    <div class="rule"></div><div class="label">Commercial</div>
  </div>
  <div class="service" style="left:414px;top:830px">
    <svg viewBox="0 0 50 50" fill="none" stroke="var(--teal)" stroke-width="1.8"><rect x="8" y="4" width="22" height="15"/><path d="M19 19v4M2 24h46M5 24v22M45 24v22"/><rect x="30" y="26" width="13" height="20"/><path d="M30 33h13M30 40h13M36 10v12"/></svg>
    <div class="rule"></div><div class="label">Office</div>
  </div>
  <div class="service" style="left:571px;top:830px">
    <svg viewBox="0 0 50 50" fill="none" stroke="var(--teal)" stroke-width="1.8"><rect x="28" y="12" width="12" height="34" rx="3"/><path d="M30 12V6h8v6M31 24h4M31 30h4M31 36h4"/><circle cx="15" cy="38" r="7"/><circle cx="15" cy="27" r="4"/></svg>
    <div class="rule"></div><div class="label">Child Care</div>
  </div>
  <div class="service" style="left:735px;top:830px">
    <svg viewBox="0 0 50 50" fill="none" stroke="var(--teal)" stroke-width="1.8"><rect x="14" y="12" width="22" height="34"/><rect x="4" y="22" width="10" height="24"/><rect x="36" y="22" width="10" height="24"/><path d="M25 3v7M21.5 6.5h7"/><rect x="21" y="36" width="8" height="10"/><path d="M18 18h4M28 18h4M18 26h4M28 26h4"/></svg>
    <div class="rule"></div><div class="label">Medical</div>
  </div>

  <div class="service" style="left:64px;top:944px">
    <svg viewBox="0 0 50 50" fill="none" stroke="var(--teal)" stroke-width="1.8"><rect x="8" y="4" width="34" height="20"/><path d="M20 10c0-3 4-3 5-1 1-2 5-2 5 1 0 4-2 5-2 9l-3-4-3 4c0-4-2-5-2-9Z"/><path d="M4 24h42v6H4zM7 30v16h36V30"/><rect x="14" y="34" width="8" height="12"/><rect x="28" y="34" width="10" height="7"/></svg>
    <div class="rule"></div><div class="label">Dental</div>
  </div>
  <div class="service" style="left:226px;top:944px">
    <svg viewBox="0 0 50 50" fill="none" stroke="var(--teal)" stroke-width="1.8"><path d="M8 30a17 17 0 0 1 34 0Z"/><circle cx="25" cy="10" r="2"/><path d="M5 30h40M4 38h14l10 6h14M8 44h8"/></svg>
    <div class="rule"></div><div class="label">Restaurant</div>
  </div>
  <div class="service" style="left:386px;top:944px">
    <svg viewBox="0 0 50 50" fill="none" stroke="var(--teal)" stroke-width="1.8"><rect x="3" y="4" width="44" height="30"/><path d="M9 4c3 10 3 20 0 30M41 4c-3 10-3 20 0 30M3 34v12h44V34M3 40h44"/></svg>
    <div class="rule"></div><div class="label">Entertainment</div>
  </div>
  <div class="service" style="left:545px;top:944px">
    <svg viewBox="0 0 50 50" fill="none" stroke="var(--teal)" stroke-width="1.8"><rect x="10" y="4" width="30" height="42"/><path d="M15 10h4v4h-4zM23 10h4v4h-4zM31 10h4v4h-4zM15 19h4v4h-4zM23 19h4v4h-4zM31 19h4v4h-4zM15 28h4v4h-4zM31 28h4v4h-4zM21 46V36h8v10M4 46h42"/></svg>
    <div class="rule"></div><div class="label">Hotel/motel</div>
  </div>
  <div class="service" style="left:723px;top:944px;width:134px">
    <svg viewBox="0 0 50 50" fill="none" stroke="var(--teal)" stroke-width="1.8"><rect x="10" y="3" width="30" height="12"/><path d="M16 12l3-5h12l3 5M5 15h40v5H5zM8 20v26h34V20"/><path d="M12 36l3-6h20l3 6v6H12z"/><circle cx="17" cy="39" r="1.5"/><circle cx="33" cy="39" r="1.5"/></svg>
    <div class="rule"></div><div class="label">Automotive Fleets</div>
  </div>

  <div class="abs call">CALL US NOW</div>
  <div class="abs phone">
    <svg viewBox="0 0 42 42"><circle cx="21" cy="21" r="20" fill="var(--blue)"/><path d="M15 11c-2 1-4 3-3 7 2 7 7 12 13 14 4 1 6-1 7-3l-4-4-3 2c-3-1-6-4-7-7l2-3Z" fill="var(--white)"/></svg>
    <span>555-847-2936</span>
  </div>
  <p class="abs tagline">Our professional spraying equipment<br>and disinfect their facilities</p>
  <div class="abs email">
    <svg viewBox="0 0 32 32"><circle cx="16" cy="16" r="15" fill="var(--white)" stroke="var(--teal-soft)" stroke-width="1.5"/><rect x="9" y="11" width="14" height="10" fill="none" stroke="var(--blue)" stroke-width="1.5"/><path d="M9 11l7 6 7-6" fill="none" stroke="var(--blue)" stroke-width="1.5"/></svg>
    <span>tormelvax@brintova.com</span>
  </div>
</main>
</body>
</html>
```